Refresh of graphic design for existing website

We would like to refresh our website. Please see the attached design specifications.

Industry/Entity Type

Graphic Design

```html
<!DOCTYPE html>
<html lang="en">
<head>
<meta charset="utf-8">
<title>The Service Gear &amp; Tool Council</title>
<link href="https://fonts.googleapis.com/css2?family=Montserrat:wght@400;600;700;800&family=Open+Sans:wght@400;600;700&display=swap" rel="stylesheet">
<style>
:root{
  --blue:#1f7fc4;
  --blue-light:#3aa4dc;
  --sky:#2b93d6;
  --teal:#1e9a82;
  --teal-dark:#116a5e;
  --teal-deep:#0d4f47;
  --green:#25a35f;
  --ink:#2c2c2c;
  --grey:#777;
  --line:#d8d8d8;
  --paper:#ffffff;
  --mist:#eef3f3;
  --night:#1d2326;
}
*{box-sizing:border-box;margin:0;padding:0}
html,body{width:1200px;height:2400px;overflow:hidden}
body{font-family:"Open Sans",Arial,sans-serif;color:var(--ink);background:var(--paper);position:relative}
.h{font-family:"Montserrat",Arial,sans-serif}
section,header,nav,footer{position:absolute;left:0;width:1200px}

/* header */
.site-header{top:0;height:180px;background:linear-gradient(90deg,var(--blue) 0%,var(--blue-light) 60%,var(--sky) 100%)}
.site-title{position:absolute;left:22px;top:8px;color:#fff;font-size:38px;font-weight:700;white-space:nowrap}
.brand{position:absolute;left:24px;top:70px;display:flex;align-items:center;gap:18px}
.brand-mark{width:64px;height:64px;border-radius:50%;background:#fff}
.brand-name{color:#fff;font-size:36px;font-weight:700;white-space:nowrap}
.tagline{position:absolute;left:120px;top:140px;color:#fff;font-size:13px;font-weight:600;border-top:2px solid rgba(255,255,255,.7);padding-top:4px;width:420px}
.login{position:absolute;right:24px;top:46px;width:300px}
.login .row{display:flex;gap:8px;margin-bottom:8px}
.login input{flex:1;min-width:0;height:26px;border:0;padding:0 8px;font-size:11px;font-family:inherit}
.login label{color:#fff;font-size:11px;display:flex;align-items:center;gap:6px;margin-bottom:8px}
.login .box{width:12px;height:12px;background:#fff}
.btn-login{display:block;width:100%;height:28px;background:var(--green);color:#fff;border:0;font-weight:700;font-size:12px;letter-spacing:1px}

/* nav */
.main-nav{top:180px;height:52px;background:var(--teal-dark);display:flex;align-items:center;padding:0 30px}
.main-nav a{color:#fff;text-decoration:none;font-size:12px;font-weight:700;margin-right:46px;letter-spacing:.5px;white-space:nowrap}
.nav-social{margin-left:auto;display:flex;gap:10px}
.nav-social span,.foot-social span{width:24px;height:24px;border-radius:50%;border:2px solid #fff;display:block}

/* hero */
.hero{top:232px;height:570px;background:linear-gradient(160deg,#3d4a55 0%,#1d2a33 45%,#6a4a2e 80%,#2a2a2a 100%)}
.hero-title{position:absolute;left:0;right:0;top:200px;text-align:center;color:#fff;font-size:84px;font-weight:800;line-height:1.05}
.hero-title .amp{font-size:110px;position:relative;top:10px}
.dots{display:flex;gap:10px;justify-content:center}
.dots i{width:12px;height:12px;border-radius:50%;background:rgba(255,255,255,.5);display:block}
.dots i.on{background:#fff}
.hero .dots{position:absolute;bottom:20px;left:0;right:0}
.search-band{top:802px;height:70px;background:#1b2125;display:flex;align-items:center;justify-content:center;gap:16px}
.search-band b{color:#fff;font-size:16px;letter-spacing:1px}
.search-band .field{width:200px;height:28px;background:#fff;font-size:11px;color:#999;padding:6px 10px}

/* welcome + news */
.intro{top:880px;height:360px}
.welcome{position:absolute;left:50px;top:50px;width:560px}
.sec-title{font-size:34px;font-weight:700;color:#333}
.sec-title em{font-style:normal;color:var(--blue)}
.welcome p{margin-top:22px;font-size:13px;line-height:1.75;color:var(--grey)}
.btn-read{display:inline-block;margin-top:26px;background:var(--green);color:#fff;font-size:12px;font-weight:700;padding:12px 22px}
.upcoming{position:absolute;left:660px;top:50px;width:490px}
.view-all{position:absolute;right:0;top:14px;font-size:12px;color:var(--blue)}
.news-item{display:flex;gap:16px;margin-top:26px}
.news-photo{width:84px;height:84px;background:linear-gradient(135deg,#9aa3a8,#5e6a70);flex:none}
.news-item h3{font-size:16px;font-weight:700;color:#333}
.news-item p{font-size:12px;color:var(--grey);line-height:1.5;margin-top:4px}
.news-item + .news-item{border-top:1px solid var(--line);padding-top:20px}

/* events */
.events{top:1250px;height:370px;background:var(--teal)}
.arrow{position:absolute;top:170px;color:#fff;font-size:34px;font-weight:700}
.event{position:absolute;top:40px;width:260px;height:290px;background:var(--mist);text-align:center;overflow:hidden}
.event .name{font-size:36px;font-weight:800;color:var(--teal);margin-top:26px;white-space:nowrap}
.event .lead{font-size:14px;font-weight:700;color:#333;padding:12px 22px 0;line-height:1.35}
.event .date{margin:18px 0 0;background:var(--teal);color:#fff;font-size:13px;font-weight:700;padding:10px 16px;line-height:1.35}
.event .note{font-size:12px;font-weight:700;color:#333;padding:12px 20px 0;line-height:1.35}
.event-photo{background:linear-gradient(160deg,#9fb2bf 0%,#d5dee3 45%,#6c7f6a 100%)}
.event-photo .more{position:absolute;left:0;right:0;bottom:0;height:44px;background:var(--teal-dark);color:#fff;font-weight:700;font-size:14px;line-height:44px}
.events .dots{position:absolute;bottom:14px;left:0;right:0}

/* quick links */
.quick{top:1640px;height:210px}
.quick .sec-title{text-align:center;margin-top:20px}
.quick-row{position:absolute;top:110px;left:40px;right:40px;display:flex;gap:14px}
.quick-row a{flex:1;border:1px solid var(--line);height:44px;display:flex;align-items:center;justify-content:center;text-align:center;font-size:11px;color:#555;text-decoration:none;padding:0 6px}
.quick-row a.on{background:var(--teal);color:#fff;border-color:var(--teal)}
.quick .dots{position:absolute;top:178px;left:0;right:0}
.quick .dots i{background:#cfd6d6}.quick .dots i.on{background:var(--teal)}

/* industry news */
.industry{top:1860px;height:320px;background:var(--night)}
.industry-photo{position:absolute;left:0;top:0;width:560px;height:320px;background:linear-gradient(135deg,#2e3a42,#11171a)}
.industry-photo h2{position:absolute;left:0;right:0;top:140px;text-align:center;color:#fff;font-size:32px;font-weight:800}
.story{position:absolute;left:590px;top:34px;width:580px;display:flex;gap:20px}
.story-photo{width:150px;height:160px;background:linear-gradient(160deg,#6b7378,#3a4146);flex:none}
.story h3{color:#fff;font-size:16px;font-weight:700}
.story p{color:#b8bec1;font-size:12px;line-height:1.6;margin-top:10px}
.story .read{display:block;text-align:right;color:#fff;font-size:11px;margin-top:10px}
.industry .dots{position:absolute;left:590px;right:0;bottom:26px}

/* social */
.social{top:2190px;height:130px;display:flex}
.social .col{flex:1;padding:26px 40px;color:#fff}
.social .c1{background:var(--sky)}.social .c2{background:var(--blue-light)}.social .c3{background:var(--teal-dark)}
.social .tag{display:flex;align-items:center;gap:14px;font-size:30px;font-weight:600}
.social .tag span{width:34px;height:34px;border-radius:50%;background:rgba(255,255,255,.85)}
.social .meta{display:flex;justify-content:space-between;margin-top:14px;font-size:11px;opacity:.9}

.site-footer{top:2320px;height:80px;background:var(--teal-deep);color:#cfe3df;text-align:center;font-size:11px;padding-top:20px}
.site-footer nav{position:static;width:auto;display:block;margin-bottom:8px}
.site-footer nav a{color:#fff;text-decoration:none;margin:0 8px}
.foot-social{position:absolute;right:30px;top:26px;display:flex;gap:8px}
</style>
</head>
<body>

<header class="site-header">
  <div class="site-title">The Service Gear &amp; Tool Council</div>
  <div class="brand"><span class="brand-mark"></span><span class="brand-name h">www.sgtcouncil.org</span></div>
  <div class="tagline">Serving the automotive repair industry since 1947</div>
  <form class="login">
    <div class="row"><input type="text" placeholder="Email"><input type="password" placeholder="Password"></div>
    <label><span class="box"></span>Remember me</label>
    <button class="btn-login" type="button">LOGIN</button>
  </form>
</header>

<nav class="main-nav h">
  <a href="#">HOME</a><a href="#">ABOUT SGTC</a><a href="#">NEWS</a><a href="#">MEMBERSHIP</a><a href="#">EVENTS</a><a href="#">MEMBERS ONLY</a><a href="#">INDUSTRY OUTREACH</a>
  <div class="nav-social"><span></span><span></span><span></span></div>
</nav>

<section class="hero" role="img" aria-label="Photo of a car driving on a road at dusk with light trails">
  <h1 class="hero-title h">THE SERVICE GEAR <span class="amp">&amp;</span><br>TOOL COUNCIL</h1>
  <div class="dots"><i class="on"></i><i></i><i></i></div>
</section>

<section class="search-band h"><b>SITE SEARCH</b><div class="field">Enter search keywords</div></section>

<section class="intro">
  <div class="welcome">
    <h2 class="sec-title h">WELCOME TO <em>SGTC</em></h2>
    <p>Our council brings together the makers of tools, equipment and information that keep repair shops running. Members work side by side to share service data, support training and help technicians fix today's vehicles with confidence. For decades we have linked vehicle makers with the aftermarket, building programs that make repair faster, safer and more accurate. Join us at our events, explore our resources and see how our members move the service industry forward every single day.</p>
    <span class="btn-read h">READ MORE</span>
  </div>
  <div class="upcoming">
    <h2 class="sec-title h">UPCOMING <em>NEWS</em></h2>
    <span class="view-all">View All</span>
    <div class="news-item">
      <div class="news-photo" role="img" aria-label="Portrait photo of a speaker"></div>
      <div><h3 class="h">Lorem Ipsum Dolor Sit</h3><p>Short update on member activity, upcoming meetings and new training programs for shops this season.</p></div>
    </div>
    <div class="news-item">
      <div class="news-photo" role="img" aria-label="Portrait photo of a council officer"></div>
      <div><h3 class="h">Lorem Ipsum Dolor Sit</h3><p>Brief note on industry news, tool standards work and plans shared at the last council meeting.</p></div>
    </div>
  </div>
</section>

<section class="events h">
  <span class="arrow" style="left:28px">&lsaquo;</span>
  <span class="arrow" style="right:28px">&rsaquo;</span>
  <article class="event" style="left:70px">
    <div class="name">SHOP WEEK</div>
    <div class="lead">REGISTRATION NOW OPEN FOR WINTER SHOP WEEK 2015</div>
    <div class="date">DECEMBER 2-4 IN SEACREST BEACH, CA</div>
  </article>
  <article class="event event-photo" style="left:340px" role="img" aria-label="Photo of a silver car on a sunny road">
    <div class="more">READ MORE &rsaquo;</div>
  </article>
  <article class="event" style="left:610px">
    <div class="name">GEAR EXPO</div>
    <div class="lead">SAVE THE DATE FOR GEAREXPO 2016</div>
    <div class="date">MAY 12-15 IN BAYVIEW HARBOR, CA</div>
    <div class="note">AUTOMOTIVE TECHNOLOGY LIVE IN THE FAST LANE</div>
  </article>
  <article class="event" style="left:880px">
    <div class="name">SHOP WEEK</div>
    <div class="lead">REGISTRATION NOW OPEN FOR WINTER SHOP WEEK 2015</div>
    <div class="date">DECEMBER 2-4 IN SEACREST BEACH, CA</div>
  </article>
  <div class="dots"><i class="on"></i><i></i></div>
</section>

<section class="quick">
  <h2 class="sec-title h">QUICK <em>LINK</em></h2>
  <div class="quick-row">
    <a href="#">Service Data Library</a><a href="#">SGTC Blog</a><a href="#" class="on">SGTC Member Companies</a><a href="#">SGTC Jobs Bulletin</a><a href="#">Investment Planning Guide</a><a href="#">SGTC Member Product Gallery</a>
  </div>
  <div class="dots"><i class="on"></i><i></i></div>
</section>

<section class="industry">
  <div class="industry-photo" role="img" aria-label="Dark photo of a technician working on a vehicle engine"><h2 class="h">INDUSTRY NEWS</h2></div>
  <div class="story">
    <div class="story-photo" role="img" aria-label="Portrait photo of an industry author"></div>
    <div>
      <h3 class="h">HOW SHOPS IMPACT CAR BUYING DECISIONS</h3>
      <p>A new survey shows that drivers trust their repair shop when choosing a next car. Service advice, fair prices and clear answers shape how owners view a brand long after the sale. Shops that invest in tools and training earn more loyal customers.</p>
      <span class="read">READ MORE &rsaquo;</span>
    </div>
  </div>
  <div class="dots"><i></i><i class="on"></i><i></i></div>
</section>

<section class="social">
  <div class="col c1"><div class="tag"><span></span>Friends Page</div><div class="meta"><span>sgtcouncil page</span><span>1200 Likes</span></div></div>
  <div class="col c2"><div class="tag"><span></span>Short Posts</div><div class="meta"><span>@sgtcouncil</span><span>1200 Followers</span></div></div>
  <div class="col c3"><div class="tag"><span></span>Photo Feed</div><div class="meta"><span>@sgtcouncil</span><span>1200 Followers</span></div></div>
</section>

<footer class="site-footer">
  <nav><a href="#">Home</a>|<a href="#">Privacy</a>|<a href="#">Terms &amp; Conditions</a>|<a href="#">Donations</a>|<a href="#">Site Map</a></nav>
  <div>Copyright 2015 The Service Gear &amp; Tool Council. All rights reserved.</div>
  <div class="foot-social"><span></span><span></span><span></span></div>
</footer>

</body>
</html>
```